TheLedgerMist.com web site

We need a Wordpress theme for a new business we are launching called:

TheLedgerMist.com

"Real time access to currency markets for eCommerce"

You can see the logo / colours at www.theledgermist.com (the logo was designed by a SketchHive.com designer!).

Web site to be along simlar lines to our pre-launch site www.theledgermist.com

The ledger mist is a fintech / financial services company (i.e. the DNA is more tech than financial services) that has three products:

1. SaaS Currency Apps - that customers can use to run their own currency business

2. PaaS Currency API - that customers use to develop their own currency apps and / or integrate currency capabilities into their existing apps and processes

3. Currency Liquidity - direct access to the currency markets to buy/sell currency and make international payments. Forex rates are transparent, consistent and fair for all customers.

Other notes...

A more web 2.0'ish / API related brand, but still serious enough to be take seriously be CxO level decision makers.

The brand is B2B and not B2C or C2C

Please do NOT put forward canned designs found at places like layoutgoblin.com etc.

Reason: Hi,

We have increased the budget for this project - please take another look.

Regards,

Rupert

Hi,

The logo .png file has been uploaded to the design brief

Rupert

Hi,

Some feedback based on what as been submitted so far..

- the logo is designed to go on white background

- take a closer look at our existing "hacked together" site www.theledgermist.com (we like this)- take a look at the site of our owner www.brivanholdings.co.uk- you will notice the sleek, un-cluttered and professional designKindest regards,Rupert

Reason: Just so we get the finishing touches done

Target Market(s)

B2B Targets three main communities:

- financial decision makers
- product managers
- technology/ developer community (for our APIs)

Industry/Entity Type

Financial

Requirements
Must have
• Not appear to be a "blog", but a simple to manage a web site based upon a wordpress theme.

Sections for "product", "blog", "about us", "products"

Clear "call to action" buttons (contact us, sign up etc.) and social buttons

Front page to have a space for video content (as per current web site)

Must have a clear section on the front page "what can we do for you?" where we list various client types and how we can help them

Must have a clear section on the front page "what we do?" where we list the various services we do

```html
<!DOCTYPE html>
<html lang="en">
<head>
<meta charset="utf-8">
<title>TheLedgerMist.com</title>
<link href="https://fonts.googleapis.com/css2?family=Arimo:wght@400;700&display=swap" rel="stylesheet">
<style>
:root{
  --brand-blue:#4f86a5;
  --nav-active:#346985;
  --rule-light:#a9c6d6;
  --ink:#555555;
  --ink-soft:#5f5f5f;
  --white:#ffffff;
  --divider:#c8c8c8;
  --stage:#000000;
  --player-bar:#c9c9c9;
}
*{margin:0;padding:0;box-sizing:border-box}
html,body{width:1126px;height:1200px;overflow:hidden;background:var(--white)}
body{position:relative;font-family:"Arimo",Arial,sans-serif;color:var(--ink)}
.abs{position:absolute}
.header-band{left:0;top:0;width:1126px;height:319px;background:var(--brand-blue)}
.brand{left:18px;top:70px;display:flex;align-items:center;gap:8px;font-size:25px;color:#5a5a5a}
.brand-mark{width:18px;height:18px;background:#7cc1ea}
.main-nav{left:678px;top:33px;display:flex;gap:6px}
.main-nav a{color:var(--white);text-decoration:none;font-size:15.5px;padding:2px 10px}
.main-nav a.is-active{background:var(--nav-active)}
.cta-nav{top:107px;font-size:15.5px;color:var(--white)}
.header-rule{left:20px;top:128px;width:1075px;height:1px;background:var(--rule-light)}
.headline{left:0;top:136px;width:1126px;text-align:center;color:var(--white);font-size:30px;text-shadow:0 0 6px rgba(255,255,255,.7)}
.subline{left:0;top:173px;width:1126px;text-align:center;color:var(--white);font-size:15px;font-weight:700;letter-spacing:-.3px;text-shadow:0 0 5px rgba(255,255,255,.7)}
.slider{left:98px;top:225px;width:950px;height:222px;background:linear-gradient(#000 60%,#222);border:1px solid #ddd}
.slide-title{top:22px;left:0;width:100%;text-align:center;color:var(--white);font-size:30px}
.slide-art{left:405px;top:77px;width:140px;height:130px;border-radius:6px;background:linear-gradient(135deg,#f4d77a,#c98a12)}
.arrow{top:270px}
.col-title{font-size:19.5px;color:var(--ink)}
.copy{font-size:15px;line-height:19px;color:var(--ink-soft);hyphens:auto;-webkit-hyphens:auto}
.vrule{width:2px;background:var(--divider)}
.hrule{height:2px;background:var(--divider)}
.player{left:455px;top:816px;width:274px;height:224px;background:var(--stage)}
.player-bar{left:0;bottom:0;width:100%;height:19px;background:var(--player-bar)}
.footer-band{left:0;top:1067px;width:1126px;height:133px;background:var(--brand-blue);color:var(--white)}
.foot-title{font-size:15.5px}
.foot-copy{font-size:10.5px;line-height:12.8px;width:320px}
.social{top:40px;width:36px;height:36px;border-radius:4px}
.foot-rule{left:89px;top:116px;width:944px;height:1px;background:var(--rule-light)}
.legal{left:0;top:120px;width:1126px;text-align:center;font-size:10px}
</style>
</head>
<body>
<header class="abs header-band">
  <div class="abs brand"><span class="brand-mark"></span>TheLedgerMist.com</div>
  <nav class="abs main-nav">
    <a class="is-active" href="#">Home</a><a href="#">Product</a><a href="#">Blog</a><a href="#">About Us</a><a href="#">Products</a>
  </nav>
  <a class="abs cta-nav" style="left:768px">call to action...</a>
  <a class="abs cta-nav" style="left:917px">contact us</a>
  <a class="abs cta-nav" style="left:1032px">sign up</a>
  <div class="abs header-rule"></div>
  <h1 class="abs headline" style="font-weight:400">Lorem ipsum dolor sit amet, consectetur adipiscing elit.</h1>
  <p class="abs subline">Lorem ipsum dolor sit amet, consectetur adipiscing elit. Aliquam varius pellentesque venenatis. Aliquam dignissim, urna</p>
</header>

<svg class="abs arrow" style="left:70px" width="26" height="36" viewBox="0 0 26 36"><polyline points="20,4 6,18 20,32" fill="none" stroke="#b9cbd6" stroke-width="6"/></svg>
<svg class="abs arrow" style="left:1050px" width="26" height="36" viewBox="0 0 26 36"><polyline points="6,4 20,18 6,32" fill="none" stroke="#b9cbd6" stroke-width="6"/></svg>

<section class="abs slider">
  <h2 class="abs slide-title" style="font-weight:400">We got you covered</h2>
  <div class="abs slide-art" role="img" aria-label="Golden safe illustration"></div>
</section>

<h3 class="abs col-title" style="left:95px;top:460px;font-weight:400">what can we do for you ?</h3>
<p class="abs copy" style="left:97px;top:494px;width:350px">Lorem ipsum dolor sit amet, consectetur adipiscing elit. Aliquam varius pellentesque venenatis. Aliquam dignissim, urna eget mattis tincidunt, justo felis tincidunt tortor, non pulvinar lectus nibh eu diam. Ut nec mauris sed orci porta congue. Vestibulum consectetur nisi ac neque ultricies scelerisque. Nullam dictum pellentesque turpis, volutpat tempor diam interdum id. Vestibulum sed dui nunc, eget posuere orci. Aenean sollicitudin ipsum sed purus auctor sit amet vehicula tortor cursus. Vivamus nec neque sed fringilla pharetra quis eu leo. Etiam ullamcorper nunc sit amet felis ornare pretium. Maecenas posuere tincidunt nunc, lacinia scelerisque tortor suscipit in. Nunc sed augue metus. Duis ac felis</p>
<div class="abs vrule" style="left:580px;top:458px;height:338px"></div>
<h3 class="abs col-title" style="left:640px;top:460px;font-weight:400">what we do ?</h3>
<p class="abs copy" style="left:642px;top:494px;width:350px">Lorem ipsum dolor sit amet, consectetur adipiscing elit. Aliquam varius pellentesque venenatis. Aliquam dignissim, urna eget mattis tincidunt, justo felis tincidunt tortor, non pulvinar lectus nibh eu diam. Ut nec mauris sed orci porta congue. Vestibulum consectetur nisi ac neque ultricies scelerisque. Nullam dictum pellentesque turpis, volutpat tempor diam interdum id. Vestibulum sed dui nunc, eget posuere orci. Aenean sollicitudin ipsum sed purus auctor sit amet vehicula tortor cursus. Vivamus nec neque sed fringilla pharetra quis eu leo. Etiam ullamcorper nunc sit amet felis ornare pretium. Maecenas posuere tincidunt nunc, lacinia scelerisque tortor suscipit in. Nunc sed augue metus. Duis ac felis</p>

<div class="abs hrule" style="left:92px;top:802px;width:962px"></div>

<p class="abs copy" style="left:95px;top:813px;width:320px;height:228px;overflow:hidden">Lorem ipsum dolor sit amet, consectetur adipiscing elit. Aliquam varius pellentesque venenatis. Aliquam dignissim, urna eget mattis tincidunt, justo felis tincidunt tortor, non pulvinar lectus nibh eu diam. Ut nec mauris sed orci porta congue. Vestibulum consectetur nisi ac neque ultricies scelerisque. Nullam dictum pellentesque turpis, volutpat tempor diam interdum id. Vestibulum sed dui nunc, eget posuere orci. Aenean sollicitudin ipsum sed purus auctor sit amet vehicula tortor cursus. Vivamus nec neque sed</p>
<div class="abs vrule" style="left:432px;top:816px;height:233px"></div>
<div class="abs player" role="img" aria-label="Video player">
  <svg class="abs" style="left:129px;top:98px" width="16" height="16" viewBox="0 0 16 16"><circle cx="8" cy="8" r="5" fill="none" stroke="#777" stroke-width="2" stroke-dasharray="3 2"/></svg>
  <div class="abs player-bar">
    <svg width="274" height="19" viewBox="0 0 274 19">
      <rect x="5" y="5" width="3" height="9" fill="#555"/><rect x="10" y="5" width="3" height="9" fill="#555"/>
      <polygon points="30,5 30,14 23,9.5" fill="#555"/>
      <rect x="44" y="8" width="100" height="3" fill="#555"/><circle cx="46" cy="9.5" r="4" fill="#777"/>
      <rect x="150" y="3" width="48" height="13" fill="#222"/>
      <rect x="208" y="8" width="34" height="3" fill="#555"/><polygon points="246,9 254,4 254,15" fill="#555"/>
      <rect x="260" y="5" width="10" height="9" fill="#777"/>
    </svg>
  </div>
</div>
<div class="abs vrule" style="left:748px;top:816px;height:233px"></div>
<p class="abs copy" style="left:763px;top:813px;width:330px;height:228px;overflow:hidden">Lorem ipsum dolor sit amet, consectetur adipiscing elit. Aliquam varius pellentesque venenatis. Aliquam dignissim, urna eget mattis tincidunt, justo felis tincidunt tortor, non pulvinar lectus nibh eu diam. Ut nec mauris sed orci porta congue. Vestibulum consectetur nisi ac neque ultricies scelerisque. Nullam dictum pellentesque turpis, volutpat tempor diam interdum id. Vestibulum sed dui nunc, eget posuere orci. Aenean sollicitudin ipsum sed purus auctor sit amet vehicula tortor cursus. Vivamus nec neque sed</p>

<footer class="abs footer-band">
  <h4 class="abs foot-title" style="left:95px;top:3px;font-weight:400">About Us</h4>
  <p class="abs foot-copy" style="left:95px;top:21px">Lorem ipsum dolor sit amet, consectetur adipiscing elit. Aliquam varius pellentesque venenatis. Aliquam dignissim, urna eget mattis tincidunt, justo felis tincidunt tortor, non pulvinar lectus nibh eu diam. Ut nec mauris sed orci porta congue. Vestibulum consectetur nisi ac neque ultricies scelerisque. Nullam dictum pellentesque turpis, volutpat tempor diam interdum id. Vestibulum sed dui nunc, eget posuere orci. Aenean sollicitudin ipsum sed purus auctor sit</p>
  <h4 class="abs foot-title" style="left:446px;top:3px;font-weight:400">Support</h4>
  <p class="abs foot-copy" style="left:446px;top:21px">Lorem ipsum dolor sit amet, consectetur adipiscing elit. Aliquam varius pellentesque venenatis. Aliquam dignissim, urna eget mattis tincidunt, justo felis tincidunt tortor, non pulvinar lectus nibh eu diam. Ut nec mauris sed orci porta congue. Vestibulum consectetur nisi ac neque ultricies scelerisque. Nullam dictum pellentesque turpis, volutpat tempor diam interdum id. Vestibulum sed dui nunc, eget posuere orci. Aenean sollicitudin ipsum sed purus auctor sit</p>
  <h4 class="abs foot-title" style="left:798px;top:3px;font-weight:400">Connect</h4>
  <div class="abs social" style="left:794px;background:#f08a24" role="img" aria-label="Feed button"></div>
  <div class="abs social" style="left:836px;background:#2fa9e0" role="img" aria-label="Chat button"></div>
  <div class="abs social" style="left:878px;background:#9fd3dd" role="img" aria-label="Microblog button"></div>
  <div class="abs social" style="left:920px;background:#4caf50" role="img" aria-label="Profile button"></div>
  <div class="abs social" style="left:962px;background:#3b5b98" role="img" aria-label="Social network button"></div>
  <div class="abs foot-rule"></div>
  <p class="abs legal">Copyright 2011 LedgerMist. All right reserved.</p>
</footer>
</body>
</html>
```